TLV tub packaging design

Hi!
We require a design for two different flavours of packaging for a protein recovery formula.
The design will be for the cardboard tubs as in pic attached. The name of the product will be 'RD recovery formula'. The RD logo is also attached and can be slightly adjusted.
The project will require a design for the front and then a basic design for the information on the back. This will include ingredients, nutrition info, directions and production location. On the back it will also need the 'lift your stride' logo and something referring to 'RD recovery formula by 'Bright Pulse Nourish' (logo for this is attached).
The product will come in two flavours (cacao and coconut, then vanilla and acai) so will need the basic design adjusted for each flavour. The tubs are 1kg and this will need to be somewhere on the front of the tub.
This product is designed for healthy and active people, mainly female focused. The design should be clean and not overloaded with colours and pictures. It should only be two colours max. The final design should communicate that the product will assist people to reach their goals, whilst being health focused.

Target Market(s)

Active Females 20-50

Industry/Entity Type

Nutrition

Requirements
Must have
• Nutrition information and ingredients area
• Three logos attached
• Name- recovery formula
Should not have
• Not too busy, too many pictures or information. Please keep it simple.

```html
<!DOCTYPE html>
<html lang="en">
<head>
<meta charset="utf-8">
<title>RD Recovery Formula – Tub Labels</title>
<link rel="stylesheet" href="https://fonts.googleapis.com/css2?family=Bebas+Neue&family=Montserrat:wght@400;500;600;700&display=swap">
<style>
  :root {
    --page: #ffffff;
    --kraft-light: #b69a70;
    --kraft-mid: #a4814f;
    --kraft-dark: #8a6730;
    --ink: #111111;
    --paper: #ffffff;
    --rule: #3b2c16;
  }
  * { box-sizing: border-box; margin: 0; padding: 0; }
  html, body { width: 1200px; height: 1040px; overflow: hidden; background: var(--page); }
  body { position: relative; font-family: "Montserrat", sans-serif; color: var(--ink); }

  .label {
    position: absolute;
    top: 140px;
    width: 520px;
    height: 760px;
    background: linear-gradient(90deg, var(--kraft-mid) 0%, var(--kraft-light) 35%, var(--kraft-mid) 70%, var(--kraft-dark) 100%);
  }
  .label--front { left: 50px; }
  .label--back { left: 630px; }

  /* Front */
  .brand-mark {
    position: absolute; left: 50%; top: 330px; transform: translateX(-50%);
    display: flex; align-items: center; gap: 14px;
  }
  .brand-mark__dot { width: 110px; height: 110px; border-radius: 50%; background: var(--ink); }
  .brand-mark__name { font-weight: 600; font-size: 16px; letter-spacing: 3px; color: var(--ink); white-space: nowrap; }

  .product-title {
    position: absolute; left: 0; right: 0; top: 482px; text-align: center;
    font-family: "Bebas Neue", sans-serif; font-weight: 400; font-size: 62px; line-height: 1; color: var(--paper);
    white-space: nowrap;
  }
  .dots { position: absolute; left: 0; right: 0; display: flex; justify-content: center; gap: 14px; }
  .dots span { width: 13px; height: 13px; border-radius: 50%; background: var(--paper); }
  .dots--top { top: 572px; }
  .dots--bottom { top: 652px; }

  .flavour {
    position: absolute; left: 0; right: 0; top: 598px;
    display: flex; justify-content: center; align-items: center; gap: 10px;
    font-weight: 700; font-size: 23px; color: var(--ink); white-space: nowrap;
  }
  .flavour-icon { width: 48px; height: 40px; border-radius: 8px; background: #2a2014; opacity: .75; flex: none; }
  .flavour-icon--small { width: 36px; height: 30px; border-radius: 6px; }

  .net-weight {
    position: absolute; left: 0; right: 0; top: 700px; text-align: center;
    font-family: "Bebas Neue", sans-serif; font-size: 20px; color: var(--ink);
  }

  /* Back */
  .back-content {
    position: absolute; left: 35px; right: 35px; top: 302px;
    display: flex; flex-direction: column; align-items: stretch;
  }
  .facts-heading {
    display: flex; justify-content: center; align-items: center; gap: 8px;
    font-family: "Bebas Neue", sans-serif; font-weight: 400; font-size: 32px; line-height: 1; color: var(--paper);
    margin-bottom: 14px;
  }
  .facts-heading .flavour-icon { background: var(--paper); opacity: .8; }

  .facts {
    display: grid; grid-template-columns: 180px 1fr; gap: 20px;
    font-size: 11.5px; color: var(--ink);
  }
  .facts__summary p { line-height: 1.4; }
  .facts__summary .strong { font-weight: 600; }
  .facts__summary .gap { margin-top: 14px; }

  .facts-table { width: 100%; border-collapse: collapse; white-space: nowrap; }
  .facts-table th { font-weight: 600; text-align: left; padding-bottom: 3px; border-bottom: 1.5px solid var(--rule); }
  .facts-table th:last-child, .facts-table td:last-child { text-align: right; }
  .facts-table td { padding: 2px 0 1px; border-bottom: 1px solid var(--rule); line-height: 1.3; }

  .ingredients-heading {
    margin-top: 16px; text-align: center;
    font-family: "Bebas Neue", sans-serif; font-weight: 400; font-size: 32px; line-height: 1; color: var(--paper);
  }
  .ingredients-text {
    margin-top: 8px;
    font-size: 11.5px; font-weight: 600; line-height: 1.45; color: var(--ink);
  }
  .maker {
    margin-top: 12px; text-align: center;
    font-size: 12px; letter-spacing: .5px; line-height: 1.5; color: var(--paper);
  }
  .partners {
    margin-top: 12px;
    display: flex; justify-content: center; align-items: center; gap: 16px;
  }
  .partner { display: flex; align-items: center; gap: 6px; font-weight: 700; font-size: 12px; color: var(--ink); white-space: nowrap; }
  .partner__dot { width: 34px; height: 34px; border-radius: 50%; background: var(--ink); }
</style>
</head>
<body>

<section class="label label--front" aria-label="Front label">
  <div class="brand-mark">
    <div class="brand-mark__dot"></div>
    <div class="brand-mark__name">RD PERFORMANCE</div>
  </div>

  <h1 class="product-title">RD RECOVERY FORMULA</h1>

  <div class="dots dots--top"><span></span><span></span><span></span></div>
  <div class="flavour">
    <div class="flavour-icon" role="img" aria-label="Vanilla flower illustration"></div>
    <span>VANILLA + ACAI</span>
    <div class="flavour-icon" role="img" aria-label="Acai berry and leaf illustration"></div>
  </div>
  <div class="dots dots--bottom"><span></span><span></span><span></span></div>

  <p class="net-weight">NET WT 1 KG</p>
</section>

<section class="label label--back" aria-label="Back label">
  <div class="back-content">
    <h2 class="facts-heading">
      <span class="flavour-icon flavour-icon--small" role="img" aria-label="Vanilla flower illustration"></span>
      NUTRITION FACTS
      <span class="flavour-icon flavour-icon--small" role="img" aria-label="Acai berry illustration"></span>
    </h2>

    <div class="facts">
      <div class="facts__summary">
        <p class="strong">Serving Size (50g)<br>Servings per Container: 1</p>
        <p class="strong gap">Calories: 210<br>Calories from fat: 45</p>
        <p class="gap">Percent Daily Values are based on a 2,000 calorie diet. Your daily values may vary depending on your calorie needs.</p>
      </div>
      <table class="facts-table">
        <thead><tr><th>Amount Per Serving</th><th>% Daily Value</th></tr></thead>
        <tbody>
          <tr><td>Total Fat 5g</td><td>8%</td></tr>
          <tr><td>Sat. Fat 1g</td><td>5%</td></tr>
          <tr><td>Trans Fat 0g</td><td>0%</td></tr>
          <tr><td>Cholesterol 0mg</td><td></td></tr>
          <tr><td>Sodium 60mg</td><td>3%</td></tr>
          <tr><td>Total Carbohydrate 37g</td><td>12%</td></tr>
          <tr><td>Dietary Fiber 5g</td><td>20%</td></tr>
          <tr><td>Sugars 14g</td><td></td></tr>
          <tr><td>Protein 5g</td><td></td></tr>
        </tbody>
      </table>
    </div>

    <h2 class="ingredients-heading">INGREDIENTS</h2>
    <p class="ingredients-text">Lorem Ipsum is simply dummy text of the printing and typesetting industry. Lorem Ipsum has been the industry’s standard dummy text ever since the 1500s, when an unknown printer.</p>

    <p class="maker">MANUFACTURED &amp; DISTRIBUTED BY RD PERFORMANCE<br>www.rdperformancehub.com</p>

    <div class="partners">
      <div class="partner"><span class="partner__dot"></span><span>LIFT YOUR STRIDE</span></div>
      <div class="partner"><span>TLV · Bright Pulse Nourish</span></div>
    </div>
  </div>
</section>

</body>
</html>
```